Harbourgate Earthmoving – Website Design Brief

Web Design Brief

We are seeking a web designer to build a modern, responsive website for Harbourgate Earthmoving, a Sydney-based earthworks and excavation company.

2. Project Goal
- Build a professional, easy-to-navigate website that:
- Showcases HGE’s capabilities and past projects
- Attracts residential and commercial developers
- Builds credibility and encourages enquiries

3. Target Audience
- Residential developers and home builders
- Commercial construction firms
- Project managers seeking reliable excavation & plant hire services

4. Services to Highlight
- Bulk Excavation
- Detailed Excavation
- Demolition
- Shoring
- Plant Hire

5. Brand Style & Tone
- Clean, bold, and modern
- Professional with a “we get the job done” attitude
- Colors: Lime Green + Concrete Grey (from logo)
- Fonts: Match the modern, rounded, bold typeface in the logo
- Imagery: Showcase big machines, on-site work, before & after shots

6. Website Pages
Recommended structure:
- Home – Quick intro, project highlights, CTA
- About Us – Team story, mission, safety focus
- Services – Separate sections for each core service
- Projects – Case studies or photo gallery
- Plant Hire – Machines available, specs/photos
- Contact – Form + map + details

7. Assets Provided
- Logo (both long + stacked formats)
- Project photos. More can be provided if required.
- Copy: To be drafted

8. Deliverables
Responsive website (desktop/mobile/tablet)
- SEO-ready structure
- CMS (WordPress) for future edits
- Google Maps integration, job enquiry form

Target Market(s)

Target Audience Residential developers and home builders Commercial construction firms Project managers seeking reliable excavation & plant hire services

Industry/Entity Type

Construction

Number of Pages Required

1 page

Requirements
Must have
• Build a professional, easy-to-navigate website that: Showcases HGE’s capabilities and past projects Attracts residential and commercial developers Builds credibility and encourages enquiries
Nice to have
• All provided in the Description
Should not have

```html
<!DOCTYPE html>
<html lang="en">
<head>
<meta charset="utf-8">
<title>Harbourgate Earthmoving</title>
<link href="https://fonts.googleapis.com/css2?family=Michroma&family=Montserrat:wght@400;500;600;700;800&display=swap" rel="stylesheet">
<style>
:root{
  --lime:#8cc63f;
  --black:#000;
  --concrete:#5a5a5a;
  --grey:#888;
  --ink:#222;
  --muted:#666;
  --light:#ccc;
  --pill:#0e0e0e;
  --pill-line:#333;
  --white:#fff;
}
*{margin:0;padding:0;box-sizing:border-box}
html,body{width:1200px;height:3390px;overflow:hidden}
body{position:relative;background:var(--white);font-family:'Montserrat',sans-serif;color:var(--ink)}
.abs{position:absolute}
.backdrop{position:absolute;left:0;top:0;width:1200px;height:3390px}
.display{font-family:'Michroma',sans-serif;letter-spacing:2px;text-transform:uppercase;line-height:1}
.brand{color:var(--lime);font-weight:800;font-size:25px;line-height:27px;letter-spacing:1px;text-transform:uppercase}
.nav{top:26px;left:403px;display:flex;gap:25px;font-size:12px;font-weight:500;color:var(--muted)}
.nav .active{color:var(--lime);text-decoration:underline}
.call{left:772px;top:18px;display:flex;align-items:center;gap:9px}
.call .dot{width:26px;height:26px;border-radius:50%;background:var(--grey);display:flex;align-items:center;justify-content:center}
.call small{display:block;font-size:8px;color:var(--ink)}
.call b{font-size:13px;color:var(--ink)}
.btn{background:var(--grey);color:var(--white);font-size:11px;font-weight:700;letter-spacing:.5px;display:flex;align-items:center;justify-content:center;border-radius:2px}
.arrow{width:34px;height:34px;border-radius:50%;border:1px solid #bbb;display:flex;align-items:center;justify-content:center}
.photo{border-radius:6px}
.hero-title{left:408px;top:84px;font-weight:700;line-height:1.05}
.hero-title .a{color:#777;font-size:31px;display:block}
.hero-title .b{color:var(--lime);font-size:42px;display:block}
.about-text{left:155px;width:415px;font-size:12px;line-height:17.5px;color:var(--light)}
.label{font-weight:700;font-size:13px;color:var(--lime)}
.tape-big{white-space:nowrap;font-weight:700;font-size:40px;letter-spacing:1px;display:flex;gap:64px}
.tape-big .solid{color:#ddd}
.tape-big .outline{color:transparent;-webkit-text-stroke:1.3px #ddd}
.tape-band{left:-30px;width:1260px;height:58px;background:var(--lime);transform:rotate(2deg);display:flex;align-items:center;gap:40px;white-space:nowrap;font-weight:800;font-size:26px;color:var(--black);padding-left:0;letter-spacing:.5px}
.kicker{display:flex;align-items:center;gap:13px;font-size:17px;font-weight:500;letter-spacing:.5px}
.kicker i{display:block;width:63px;height:1px;background:#555}
.pill{height:49px;border:1px solid var(--pill-line);border-radius:9px;background:var(--pill);color:var(--light);font-size:31px;font-weight:500;display:flex;align-items:center;justify-content:center;letter-spacing:.5px}
.tag{position:absolute;background:var(--lime);color:var(--ink);font-size:10px;font-weight:700;padding:2px 9px;border-radius:2px}
.card-title{font-size:17px;font-weight:700;color:var(--lime)}
.card-text{font-size:11.5px;line-height:16px;color:#555;width:300px}
.field{background:var(--white);border:1px solid #ddd;border-radius:2px;font-size:10px;color:#aaa;padding:10px 12px}
.foot-head{font-size:13px;font-weight:700;color:var(--lime);letter-spacing:.5px}
.foot-item{font-size:11.5px;color:var(--light);display:flex;gap:7px;align-items:flex-start;line-height:16px}
.foot-links{font-size:11.5px;color:var(--light);line-height:20px}
.foot-links .active{color:var(--lime);text-decoration:underline}
</style>
</head>
<body>

<svg class="backdrop" viewBox="0 0 1200 3390" aria-hidden="true">
  <polygon points="0,267 1200,267 1200,1829 0,1885" fill="#000"/>
  <polygon points="0,2524 1200,2467 1200,2935 0,2935" fill="#5a5a5a"/>
  <rect x="0" y="2935" width="1200" height="418" fill="#000"/>
  <rect x="0" y="3353" width="1200" height="37" fill="#8cc63f"/>
</svg>

<!-- Header -->
<header>
  <div class="abs brand" style="left:155px;top:22px">Harbour<br>gate<br><span style="font-size:17px">Earthmoving</span></div>
  <nav class="abs nav">
    <span class="active">Home</span><span>About Us</span><span>Services</span><span>Projects</span><span>Contact Us</span>
  </nav>
  <div class="abs call">
    <span class="dot"><svg width="12" height="12" viewBox="0 0 24 24"><path d="M6.6 10.8a15 15 0 0 0 6.6 6.6l2.2-2.2a1 1 0 0 1 1-.25 11.4 11.4 0 0 0 3.6.57 1 1 0 0 1 1 1V20a1 1 0 0 1-1 1A17 17 0 0 1 3 4a1 1 0 0 1 1-1h3.5a1 1 0 0 1 1 1c0 1.25.2 2.45.57 3.57a1 1 0 0 1-.25 1z" fill="#fff"/></svg></span>
    <span><small>Call Now</small><b>(02) 5550 1872</b></span>
  </div>
  <div class="abs btn" style="left:925px;top:18px;width:118px;height:31px">GET STARTED</div>
</header>

<!-- Hero -->
<section>
  <h1 class="abs hero-title"><span class="a">DELIVERING</span><span class="b">QUALITY PROJECTS</span></h1>
  <div class="abs arrow" style="left:886px;top:100px"><svg width="10" height="10" viewBox="0 0 10 10"><path d="M6.5 1.5 3 5l3.5 3.5" fill="none" stroke="#777" stroke-width="1.2"/></svg></div>
  <div class="abs arrow" style="left:929px;top:100px"><svg width="10" height="10" viewBox="0 0 10 10"><path d="M3.5 1.5 7 5 3.5 8.5" fill="none" stroke="#777" stroke-width="1.2"/></svg></div>
  <div class="abs photo" role="img" aria-label="Orange excavator digging on a construction site" style="left:75px;top:205px;width:862px;height:407px;background:linear-gradient(160deg,#7d8a8c 0%,#a58a66 45%,#c08f5a 60%,#6f6a60 100%)"></div>
  <div class="abs photo" role="img" aria-label="Multi-storey building under construction with excavator" style="left:950px;top:205px;width:260px;height:407px;background:linear-gradient(180deg,#5d6670 0%,#8a7a66 55%,#b08c5f 100%)"></div>
</section>

<!-- About -->
<section>
  <h2 class="abs display" style="left:155px;top:714px;color:var(--lime);font-size:30px;letter-spacing:4px">About us</h2>
  <p class="abs about-text" style="top:759px">Lorem Ipsum is simply dummy text of the printing and typesetting industry. Lorem Ipsum has been the industry's standard dummy text ever since the 1500s, when an unknown printer took a galley of type and scrambled it to make a type specimen book.</p>
  <p class="abs about-text" style="top:845px">It has survived not only five centuries, but also the leap into electronic typesetting, remaining...</p>
  <div class="abs label" style="left:155px;top:902px">MISSION</div>
  <p class="abs about-text" style="top:922px">Lorem Ipsum is simply dummy text of the printing and typesetting industry. Lorem Ipsum has been the industry's text ever since the 1500s.</p>
  <div class="abs btn" style="left:155px;top:983px;width:110px;height:31px">READ MORE</div>
  <div class="abs photo" role="img" aria-label="Company pickup truck and tipper truck parked on a street" style="left:629px;top:700px;width:414px;height:322px;background:linear-gradient(180deg,#9aa3a9 0%,#b7bcbf 45%,#e5e5e5 60%,#555b5e 100%)"></div>
</section>

<!-- Service tape -->
<div class="abs tape-big" style="left:-12px;top:1130px"><span class="solid">BULK EXCAVATION</span><span class="outline">DETAILED EXCAVATION</span><span class="solid">DEMOLITION</span></div>
<div class="abs tape-band" style="top:1180px"><span style="margin-left:-10px">BULK EXCAVATION</span><span>DETAILED EXCAVATION</span><span>DEMOLITION</span><span>SHORING</span><span>PLANT HIRE</span></div>

<!-- Services -->
<section>
  <div class="abs kicker" style="left:155px;top:1340px;color:#888"><i></i>OUR EXPERTISE</div>
  <h2 class="abs display" style="left:155px;top:1368px;color:var(--white);font-size:52px;letter-spacing:3px">Services</h2>
  <div class="abs photo" role="img" aria-label="Excavators working in a deep excavation pit" style="left:128px;top:1538px;width:219px;height:244px;background:linear-gradient(180deg,#c9ccc8 0%,#a8866a 50%,#6b5a4a 100%)"></div>
  <div class="abs photo" role="img" aria-label="Yellow excavator bucket lifting soil" style="left:850px;top:1438px;width:218px;height:244px;background:linear-gradient(180deg,#7fa0b6 0%,#a39060 55%,#8a5a3a 100%)"></div>
  <div class="abs pill" style="left:439px;top:1482px;width:311px">Bulk Excavation</div>
  <div class="abs pill" style="left:412px;top:1543px;width:375px">Detailed Excavation</div>
  <div class="abs pill" style="left:472px;top:1604px;width:236px">Demolition</div>
  <div class="abs pill" style="left:495px;top:1665px;width:184px">Shoring</div>
  <div class="abs pill" style="left:479px;top:1726px;width:217px">Plant Hire</div>
</section>

<!-- Projects -->
<section>
  <div class="abs kicker" style="left:155px;top:1945px;color:#333"><i></i>OUR WORK</div>
  <h2 class="abs display" style="left:155px;top:1975px;color:var(--lime);font-size:50px;letter-spacing:3px">Projects</h2>
  <div class="abs arrow" style="left:965px;top:1986px"><svg width="10" height="10" viewBox="0 0 10 10"><path d="M6.5 1.5 3 5l3.5 3.5" fill="none" stroke="#777" stroke-width="1.2"/></svg></div>
  <div class="abs arrow" style="left:1008px;top:1986px"><svg width="10" height="10" viewBox="0 0 10 10"><path d="M3.5 1.5 7 5 3.5 8.5" fill="none" stroke="#777" stroke-width="1.2"/></svg></div>

  <article class="abs" style="left:157px;top:2059px;width:430px">
    <div style="position:relative;height:225px;border-radius:5px;overflow:hidden;display:flex">
      <div role="img" aria-label="Interior room before renovation" style="width:50%;background:linear-gradient(180deg,#a99a86,#7b6a58)"></div>
      <div role="img" aria-label="Interior room after renovation" style="width:50%;background:linear-gradient(180deg,#e8e8e6,#c9c6c0)"></div>
      <span class="tag" style="left:214px;top:170px">AFTER</span>
      <span class="tag" style="left:152px;top:188px">BEFORE</span>
    </div>
    <h3 class="card-title" style="margin:18px 0 0 25px">Lorem Ipsum Title Here</h3>
    <p class="card-text" style="margin:8px 0 0 25px">Lorem Ipsum Is Simply Dummy Text Of The Printing And Typesetting Industry.</p>
  </article>

  <article class="abs" style="left:613px;top:2059px;width:430px">
    <div style="position:relative;height:225px;border-radius:5px;overflow:hidden;display:flex">
      <div role="img" aria-label="Damaged brick house before rebuild" style="width:50%;background:linear-gradient(180deg,#6d4e3c,#4a3a30)"></div>
      <div role="img" aria-label="Rebuilt house after project" style="width:50%;background:linear-gradient(180deg,#a07a5e,#e6e4e0 60%,#8c8a80)"></div>
      <span class="tag" style="left:214px;top:170px">AFTER</span>
      <span class="tag" style="left:152px;top:188px">BEFORE</span>
    </div>
    <h3 class="card-title" style="margin:18px 0 0 26px">Lorem Ipsum Title Here</h3>
    <p class="card-text" style="margin:8px 0 0 26px">Lorem Ipsum Is Simply Dummy Text Of The Printing And Typesetting Industry.</p>
  </article>
  <svg class="abs" style="left:986px;top:2317px" width="33" height="33" viewBox="0 0 33 33" aria-hidden="true"><circle cx="16.5" cy="16.5" r="16" fill="#8cc63f"/><path d="M16.5 10v13M10 16.5h13" stroke="#fff" stroke-width="1.5"/></svg>
  <div class="abs btn" style="left:551px;top:2388px;width:96px;height:32px">VIEW ALL</div>
</section>

<!-- Quick inquiry -->
<section>
  <h2 class="abs display" style="left:0;width:1200px;text-align:center;top:2572px;color:var(--lime);font-size:30px;letter-spacing:3px">Quick Inquiry</h2>
  <div class="abs field" style="left:339px;top:2632px;width:244px;height:33px">First Name</div>
  <div class="abs field" style="left:596px;top:2632px;width:243px;height:33px">Last Name</div>
  <div class="abs field" style="left:339px;top:2675px;width:244px;height:33px">Email</div>
  <div class="abs field" style="left:596px;top:2675px;width:243px;height:33px">Phone</div>
  <div class="abs field" style="left:339px;top:2718px;width:500px;height:79px">How Can We Help?</div>
  <div class="abs btn" style="left:559px;top:2830px;width:82px;height:29px;font-size:10px">SUBMIT</div>
</section>

<!-- Service tape -->
<div class="abs tape-big" style="left:-12px;top:2968px"><span class="solid">BULK EXCAVATION</span><span class="outline">DETAILED EXCAVATION</span><span class="solid">DEMOLITION</span></div>
<div class="abs tape-band" style="top:3020px"><span style="margin-left:-10px">BULK EXCAVATION</span><span>DETAILED EXCAVATION</span><span>DEMOLITION</span><span>SHORING</span><span>PLANT HIRE</span></div>

<!-- Footer -->
<footer>
  <div class="abs brand" style="left:155px;top:3180px">Harbour<br>gate<br><span style="font-size:17px">Earthmoving</span></div>

  <div class="abs foot-head" style="left:380px;top:3152px">CONTACT US</div>
  <div class="abs" style="left:380px;top:3183px;display:flex;flex-direction:column;gap:9px">
    <div class="foot-item"><svg width="11" height="11" viewBox="0 0 24 24"><path d="M6.6 10.8a15 15 0 0 0 6.6 6.6l2.2-2.2a1 1 0 0 1 1-.25 11.4 11.4 0 0 0 3.6.57 1 1 0 0 1 1 1V20a1 1 0 0 1-1 1A17 17 0 0 1 3 4a1 1 0 0 1 1-1h3.5a1 1 0 0 1 1 1c0 1.25.2 2.45.57 3.57a1 1 0 0 1-.25 1z" fill="#8cc63f"/></svg>(02) 5550 1872</div>
    <div class="foot-item"><svg width="11" height="11" viewBox="0 0 24 24"><rect x="5" y="3" width="14" height="6" fill="#8cc63f"/><rect x="2" y="9" width="20" height="9" rx="2" fill="#8cc63f"/><rect x="6" y="14" width="12" height="7" fill="#8cc63f" stroke="#000"/></svg>(02) 5550 1873</div>
    <div class="foot-item"><svg width="11" height="11" viewBox="0 0 24 24"><rect x="2" y="5" width="20" height="14" rx="2" fill="#8cc63f"/><path d="M2 6l10 7 10-7" fill="none" stroke="#000" stroke-width="1.5"/></svg>info@harbourgateearthmoving.com</div>
    <div class="foot-item"><svg width="11" height="13" viewBox="0 0 24 28"><path d="M12 1a9 9 0 0 0-9 9c0 7 9 17 9 17s9-10 9-17a9 9 0 0 0-9-9z" fill="#8cc63f"/><circle cx="12" cy="10" r="3.5" fill="#000"/></svg>Unit 4/118 Quarry Lane,<br>Marlow Park NSW 2199, Aus</div>
  </div>

  <div class="abs foot-head" style="left:612px;top:3152px">QUICK LINKS</div>
  <div class="abs foot-links" style="left:612px;top:3179px">
    <div class="active">Home</div><div>About Us</div><div>Services</div><div>Projects</div><div>Contact Us</div><div>Job Enquiry</div>
  </div>

  <div class="abs" role="img" aria-label="Map of the Sydney area showing the office location" style="left:793px;top:3151px;width:250px;height:148px;border-radius:4px;background:linear-gradient(135deg,#a9d4ec 0%,#e9eef0 45%,#f3f1ec 100%)"></div>

  <div class="abs" style="left:155px;top:3364px;font-size:10.5px;color:var(--white);font-weight:500">© 2025 Harbourgate Earthmoving. All Right Reserved</div>
  <div class="abs" style="left:946px;top:3363px;display:flex;gap:9px" aria-label="Social links">
    <span style="width:12px;height:12px;border-radius:50%;background:#fff;display:block"></span>
    <span style="width:12px;height:12px;border-radius:50%;background:#fff;display:block"></span>
    <span style="width:12px;height:12px;border-radius:50%;background:#fff;display:block"></span>
    <span style="width:12px;height:12px;border-radius:50%;background:#fff;display:block"></span>
  </div>
</footer>

</body>
</html>
```